R&T Builders and Spaces Business Card

We need to redesign our business card. We had used white vellum wih grey logo and txt in the past. I would like to bring a little life into our cards without being over the top. I think I will be going away from the vellum and printing soft touch business cards.
I have attached what we currently have and our new logo design.

```html
<!DOCTYPE html>
<html lang="en">
<head>
<meta charset="utf-8">
<title>R&amp;T Builders and Spaces — Business Card</title>
<link href="https://fonts.googleapis.com/css2?family=Montserrat:wght@400;500;600&family=Josefin+Sans:wght@300&display=swap" rel="stylesheet">
<style>
  :root {
    --stage: #3a3a3a;
    --paper: #ffffff;
    --ink: #2b2b2e;
    --ink-soft: #3c3c44;
    --rule: #d6d6d6;
    --charcoal: #262626;
    --charcoal-light: #333333;
    --mark-dark: #2e2e2e;
    --mark-light: #ffffff;
  }
  * { box-sizing: border-box; margin: 0; padding: 0; }
  html, body { width: 1200px; height: 1200px; overflow: hidden; }
  body {
    background: var(--stage);
    font-family: "Montserrat", Arial, sans-serif;
    position: relative;
  }
  .card {
    position: absolute;
    left: 160px;
    width: 880px;
    height: 503px;
    border-radius: 38px;
    overflow: hidden;
  }
  .card--front { top: 70px; background: var(--paper); color: var(--ink); }
  .card--back {
    top: 627px;
    background: linear-gradient(135deg, var(--charcoal-light), var(--charcoal) 55%);
    color: var(--mark-light);
  }

  .identity { position: absolute; left: 70px; top: 235px; }
  .identity__name {
    font-weight: 600;
    font-size: 38px;
    letter-spacing: 0.5px;
    line-height: 1;
    text-transform: uppercase;
  }
  .identity__role {
    font-weight: 500;
    font-size: 21px;
    letter-spacing: 0.5px;
    text-transform: uppercase;
    margin-top: 6px;
    color: var(--ink-soft);
  }
  .contact { list-style: none; margin-top: 28px; }
  .contact__item {
    display: flex;
    align-items: flex-start;
    gap: 12px;
    font-size: 16.5px;
    font-weight: 500;
    letter-spacing: 0.6px;
    line-height: 1.3;
    text-transform: uppercase;
    color: var(--ink-soft);
    margin-bottom: 6px;
  }
  .contact__icon { width: 18px; height: 18px; flex: none; margin-top: 2px; fill: var(--ink-soft); }
  .contact__sep { display: inline-flex; align-items: center; gap: 8px; margin-left: 10px; }

  .divider {
    position: absolute;
    left: 540px; top: 150px;
    width: 1px; height: 200px;
    background: var(--rule);
  }

  .brand {
    position: absolute;
    display: flex;
    flex-direction: column;
    align-items: flex-start;
    gap: 14px;
  }
  .brand__square { display: block; }
  .brand__name {
    font-family: "Josefin Sans", "Montserrat", sans-serif;
    font-weight: 300;
    text-transform: uppercase;
    letter-spacing: 2px;
    line-height: 1.2;
  }
  .card--front .brand { left: 610px; top: 120px; }
  .card--front .brand__square { width: 170px; height: 170px; background: var(--mark-dark); }
  .card--front .brand__name { font-size: 19px; color: var(--mark-dark); }

  .card--back .brand { left: 320px; top: 90px; }
  .card--back .brand__square { width: 240px; height: 240px; background: var(--mark-light); }
  .card--back .brand__name { font-size: 26px; color: var(--mark-light); }
</style>
</head>
<body>

<section class="card card--front" aria-label="Business card front">
  <div class="identity">
    <h1 class="identity__name">Dana M. Whitford</h1>
    <p class="identity__role">Principal</p>
    <ul class="contact">
      <li class="contact__item">
        <svg class="contact__icon" viewBox="0 0 24 24" aria-hidden="true"><path d="M6.6 10.8a15.2 15.2 0 0 0 6.6 6.6l2.2-2.2c.3-.3.7-.4 1-.2 1.1.4 2.3.6 3.6.6.6 0 1 .4 1 1V20c0 .6-.4 1-1 1C10.6 21 3 13.4 3 4c0-.6.4-1 1-1h3.5c.6 0 1 .4 1 1 0 1.3.2 2.5.6 3.6.1.3 0 .7-.2 1z"/></svg>
        <span>555 014 2730</span>
        <span class="contact__sep">
          <svg class="contact__icon" viewBox="0 0 24 24" aria-hidden="true"><path d="M7 1h10a2 2 0 0 1 2 2v18a2 2 0 0 1-2 2H7a2 2 0 0 1-2-2V3a2 2 0 0 1 2-2zm0 3v14h10V4zm5 15.5a1 1 0 1 0 0 2 1 1 0 0 0 0-2z"/></svg>
          555 018 4412
        </span>
      </li>
      <li class="contact__item">
        <svg class="contact__icon" viewBox="0 0 24 24" aria-hidden="true"><path d="M2 5h20v14H2zm2 2v.4l8 5.2 8-5.2V7zm0 2.8V17h16V9.8l-8 5.2z"/></svg>
        <span>danaw@rtbuilders.com</span>
      </li>
      <li class="contact__item">
        <svg class="contact__icon" viewBox="0 0 24 24" aria-hidden="true"><path d="M12 2a10 10 0 1 0 0 20 10 10 0 0 0 0-20zm6.9 6h-2.9a15 15 0 0 0-1.4-3.6A8 8 0 0 1 18.9 8zM12 4c.8 1.2 1.5 2.5 1.9 4h-3.8c.4-1.5 1.1-2.8 1.9-4zM4.3 14a8 8 0 0 1 0-4h3.4a16 16 0 0 0 0 4zm.8 2h2.9c.3 1.3.8 2.5 1.4 3.6A8 8 0 0 1 5.1 16zM8 8H5.1a8 8 0 0 1 4.3-3.6C8.8 5.5 8.3 6.7 8 8zm4 12c-.8-1.2-1.5-2.5-1.9-4h3.8c-.4 1.5-1.1 2.8-1.9 4zm2.3-6H9.7a14 14 0 0 1 0-4h4.6a14 14 0 0 1 0 4zm.3 5.6c.6-1.1 1.1-2.3 1.4-3.6h2.9a8 8 0 0 1-4.3 3.6zm1.7-5.6a16 16 0 0 0 0-4h3.4a8 8 0 0 1 0 4z"/></svg>
        <span>www.rtbuilders.com</span>
      </li>
      <li class="contact__item">
        <svg class="contact__icon" viewBox="0 0 24 24" aria-hidden="true"><path d="M12 2a7 7 0 0 0-7 7c0 5 7 13 7 13s7-8 7-13a7 7 0 0 0-7-7zm0 9.5A2.5 2.5 0 1 1 12 6.5a2.5 2.5 0 0 1 0 5z"/></svg>
        <span>420 W Harbor Ave, St. 310<br>Tucson, Arizona 85701</span>
      </li>
    </ul>
  </div>

  <div class="divider" aria-hidden="true"></div>

  <div class="brand">
    <span class="brand__square" aria-hidden="true"></span>
    <p class="brand__name">R&amp;T Builders<br>and Spaces</p>
  </div>
</section>

<section class="card card--back" aria-label="Business card back">
  <div class="brand">
    <span class="brand__square" aria-hidden="true"></span>
    <p class="brand__name">R&amp;T Builders and Spaces</p>
  </div>
</section>

</body>
</html>
```